Mrs. VoltBuddy - Product/Sale/Promotional Flyer

Our company Mrs.VoltBuddy are looking for a strong and effective flyer to send to potential new customers. The goal is to send flyers to our target audience (restaurants/diners/bars/hotels) with a promo code on the flyer. This promo code can be entered in to our website for a 25% discount! However, the main purpose of choosing ArtFlockly is to get a design that clearly articulates and shows the advantages of the Mrs.VoltBuddy and how it can help thier business and their customers. Can you please visit our website www.MrsVoltBuddy.example to understand more about the product. The main purpose of this flyer is for the bundle (4 charger stands, charging dock, locks and multi charging cables) you will see this “bundle” in the online store. I’m also open to any suggestions and any questions you have so please contact me! Thanks.

Target Market(s)

Cafés / Diners / Restaurants / Bars / Hotels /

Requirements
Must have
• Price of the bundle (see website/brief)
• Place on the flyer for a discount code
• The target audience must clearly and presicely understand the advantage of having their * MENUS / SPECIAL OFFERS / EVENTS OR ADVERTISEMENTS * on display while letting their customers charge their device - A win win for everyone!
• Those words do not exactly have to be used but I would like this portrayed in a way that makes it stand out to the business owner and will entice them to go online and try their first bundle for their business and their customers!
• Website: www.MrsVoltBuddy.example

```html
<!DOCTYPE html>
<html lang="en">
<head>
<meta charset="utf-8">
<title>Mrs. VoltBuddy – Special Deal Flyer</title>
<link rel="stylesheet" href="https://fonts.googleapis.com/css2?family=Roboto:ital,wght@0,400;0,500;0,700;0,900;1,400&family=Bebas+Neue&family=Lato:wght@400;700&display=swap">
<style>
:root{
  --blue:#29a8e0;
  --black:#1b1b1b;
  --grey:#a7a7a7;
  --line:#d0d0d0;
  --white:#ffffff;
  --page:#e2e2e2;
  --ink:#1e1e1e;
}
*{margin:0;padding:0;box-sizing:border-box}
html,body{width:1200px;height:1200px;overflow:hidden;background:var(--page)}
body{font-family:"Roboto",sans-serif;color:var(--ink)}
.flyer{position:absolute;left:190px;top:26px;width:820px;height:1148px;background:var(--white)}
.brand{position:absolute;left:0;top:0;width:455px;height:204px;border-bottom:2px solid var(--line);display:flex;flex-direction:column;align-items:center;justify-content:center;gap:10px}
.brand-mark{display:flex;align-items:center;gap:10px}
.brand-dot{width:30px;height:30px;border-radius:50%;background:var(--blue)}
.brand-name{font-family:"Roboto",sans-serif;font-weight:700;font-size:34px;color:var(--ink)}
.brand-url{font-size:9px;color:var(--blue);font-family:"Roboto",sans-serif}
.ph{position:absolute;border-radius:4px}
.hero-product{left:188px;top:210px;width:136px;height:262px;background:linear-gradient(180deg,#2a2a2a 0%,#5a3a2a 55%,#b9b9b9 90%)}
.product-banner{position:absolute;left:0;top:475px;width:455px;height:60px}
.product-banner svg{position:absolute;left:0;top:0}
.product-tag{position:absolute;left:96px;top:12px;font-weight:700;font-size:24px;color:var(--white)}
.product-name{position:absolute;left:214px;top:4px;font-weight:500;font-size:16px;color:var(--ink)}
.product-line{position:absolute;left:214px;top:25px;font-style:italic;font-size:12px;line-height:14px;color:var(--ink)}
.rule{position:absolute;left:0;top:536px;width:455px;height:7px;background:var(--black)}
.item-img-cover{left:28px;top:570px;width:165px;height:132px;background:linear-gradient(135deg,#c9b8a2,#4a3a32)}
.item-img-cable{left:272px;top:570px;width:140px;height:132px;background:linear-gradient(180deg,#e8e8e8,#9c9c9c)}
.item-img-bundle{left:28px;top:789px;width:170px;height:169px;background:linear-gradient(135deg,#d6d2c8,#3d3a36)}
.item-img-charger{left:300px;top:789px;width:90px;height:169px;background:linear-gradient(180deg,#4b3b32,#9a9a9a)}
.item-title{position:absolute;font-weight:700;font-size:12.5px;color:var(--ink);white-space:nowrap}
.item-title span{color:var(--blue);font-weight:500}
.price{position:absolute;width:178px;height:26px;display:flex}
.price-label{width:78px;background:var(--black);color:var(--white);font-weight:700;font-size:18px;text-align:center;line-height:26px}
.price-value{flex:1;background:var(--blue);color:var(--white);font-weight:700;font-size:20px;text-align:center;line-height:26px}
.call{position:absolute;left:0;top:1051px;width:455px;height:97px;background:var(--black);text-align:center;padding-top:15px;font-family:"Lato",sans-serif}
.call-kicker{color:var(--blue);font-weight:700;font-size:19px;line-height:22px}
.call-number{color:var(--white);font-weight:700;font-size:25px;line-height:30px}
.deal{position:absolute;left:455px;top:0;width:365px;height:1148px;background:var(--black);overflow:hidden}
.deal-bg{position:absolute;left:0;top:0}
.headline{position:absolute;left:15px;top:26px;font-weight:900;color:var(--white);font-size:78px;line-height:78px;letter-spacing:1px}
.headline-blue{position:absolute;left:15px;top:96px;font-weight:900;color:var(--blue);font-size:128px;line-height:120px;letter-spacing:1px}
.promo-box{position:absolute;left:17px;top:235px;width:316px;height:308px;border:3px solid #5d5d5d;background:var(--black)}
.sale{position:absolute;left:30px;top:30px;font-family:"Bebas Neue",sans-serif;font-size:76px;line-height:70px;color:var(--white)}
.sale .hl{color:var(--blue)}
.off{position:absolute;left:30px;top:98px;font-family:"Bebas Neue",sans-serif;font-size:90px;line-height:80px;color:var(--white)}
.promo-code{position:absolute;left:35px;top:187px;font-weight:700;font-size:17px;color:var(--white)}
.promo-text{position:absolute;left:32px;top:222px;width:248px;font-size:9.5px;line-height:12.5px;color:var(--white);text-align:justify}
.charge-scene{left:46px;top:560px;width:240px;height:238px;background:linear-gradient(160deg,rgba(120,90,60,.55),rgba(200,200,200,.55))}
.about-title{position:absolute;left:17px;top:810px;font-weight:700;font-size:21px;color:var(--white)}
.about-text{position:absolute;left:17px;top:842px;width:330px;font-size:11px;line-height:14.5px;color:var(--white);text-align:justify;font-family:"Lato",sans-serif}
.about-text p+p{margin-top:14px}
.visit{position:absolute;left:17px;top:1045px;font-family:"Lato",sans-serif;font-weight:700;font-size:21px;color:var(--black)}
.url-box{position:absolute;left:15px;top:1071px;width:317px;height:36px;background:var(--black);color:var(--white);font-family:"Lato",sans-serif;font-size:19px;text-align:center;line-height:36px}
</style>
</head>
<body>
<main class="flyer">
  <header class="brand">
    <div class="brand-mark"><span class="brand-dot"></span><span class="brand-name">Mrs. VoltBuddy</span></div>
    <div class="brand-url">www.MrsVoltBuddy.example</div>
  </header>

  <div class="ph hero-product" role="img" aria-label="Menu charging stand displaying a steak restaurant menu"></div>

  <div class="product-banner">
    <svg width="455" height="60" viewBox="0 0 455 60">
      <polygon points="157,60 190,0 434,0 402,60" fill="var(--grey)"/>
      <polygon points="72,38 92,0 201,0 181,38" fill="var(--blue)"/>
    </svg>
    <div class="product-tag">Product</div>
    <div class="product-name">Mrs. VoltBuddy</div>
    <div class="product-line">Serve your customers with a charge<br>today with Mrs. VoltBuddy!</div>
  </div>
  <div class="rule"></div>

  <div class="ph item-img-cover" role="img" aria-label="Charging stands with customised cover designs"></div>
  <div class="item-title" style="left:28px;top:708px">CUSTOMISED <span>COVER DESIGN</span></div>
  <div class="price" style="left:28px;top:731px"><div class="price-label">Price</div><div class="price-value">€19.99</div></div>

  <div class="ph item-img-cable" role="img" aria-label="Braided multi-charging cable with three connectors"></div>
  <div class="item-title" style="left:263px;top:708px">MULTI-CHARGING <span>CABLE</span></div>
  <div class="price" style="left:263px;top:731px"><div class="price-label">Price</div><div class="price-value">€7.99</div></div>

  <div class="ph item-img-bundle" role="img" aria-label="Bundle of four charger stands on a charging dock with cables"></div>
  <div class="item-title" style="left:28px;top:973px">MRS. VOLTBUDDY <span>CHARGER BUNDLE</span></div>
  <div class="price" style="left:28px;top:996px"><div class="price-label">Price</div><div class="price-value">€239.00</div></div>

  <div class="ph item-img-charger" role="img" aria-label="Single charger stand with coffee menu cover"></div>
  <div class="item-title" style="left:263px;top:973px">MRS. VOLTBUDDY <span>CHARGER</span></div>
  <div class="price" style="left:263px;top:996px"><div class="price-label">Price</div><div class="price-value">€39.00</div></div>

  <footer class="call">
    <div class="call-kicker">FOR FREE CALL</div>
    <div class="call-number">Lorem ipsum dummy</div>
  </footer>

  <section class="deal">
    <svg class="deal-bg" width="365" height="1148" viewBox="0 0 365 1148">
      <polygon points="0,503 365,669 365,1148 0,1148" fill="var(--blue)"/>
    </svg>
    <div class="headline">SPECIAL</div>
    <div class="headline-blue">DEAL</div>

    <div class="promo-box">
      <div class="sale"><span class="hl">SALE</span> UPTO</div>
      <div class="off">25% OFF</div>
      <div class="promo-code">PROMO CODE- Lorem ipsum</div>
      <p class="promo-text">Provide a better service by handing them a Mrs.VoltBuddy – Promote your own business with a custom flyer inside to promote food/drink or offers and get a happy customer who will come back!</p>
    </div>

    <div class="ph charge-scene" role="img" aria-label="Charger stand with drinks menu charging a smartphone"></div>

    <h2 class="about-title">ABOUT US</h2>
    <div class="about-text">
      <p>Mrs.VoltBuddy's goal is to provide certainty that you will never run out of battery wherever you are! We use our phones a lot... You are also on the move a lot! We want a solution for people in restaurants, cafes, hotels and bars that people can reply on! By calling in to a presmies that can serve you with a Mrs.VoltBuddy you can sit down with your phone charging my your side.</p>
      <p>By building up a network of menu power banks in cafes, restaurants and bars, we can help you find somewhere to charge your phone while having a beverage or snack – Benefiting you and the business that can provide you with a better service!</p>
    </div>

    <div class="visit">Visit our website for a discount!</div>
    <div class="url-box">www.mrsvoltbuddy.example</div>
  </section>
</main>
</body>
</html>
```